Granite, Zinc and Clay Roofing LLC needs a new business card

I need a new business card because I have a new address.
I do slate copper and tile roofs. My webpage is: www.granitezincandclayroofing.example

```html
<!DOCTYPE html>
<html lang="en">
<head>
<meta charset="utf-8">
<title>Granite, Zinc &amp; Clay Roofing — Business Card</title>
<link rel="stylesheet" href="https://fonts.googleapis.com/css2?family=Arimo:wght@400;500&display=swap">
<style>
  :root {
    --page: #c9cccd;
    --sky: #5bb8e8;
    --sky-deep: #4fb0e4;
    --ink: #0c0c0c;
    --paper-white: #ffffff;
    --divider: #b8bcbe;
    --text-font: "Arimo", Arial, sans-serif;
  }
  * { box-sizing: border-box; margin: 0; padding: 0; }
  html, body {
    width: 1187px;
    height: 1200px;
    overflow: hidden;
    background: var(--page);
    font-family: var(--text-font);
  }
  .canvas { position: relative; width: 1187px; height: 1200px; }

  .card {
    position: absolute;
    border-radius: 16px;
    overflow: hidden;
  }

  /* Front */
  .card--front {
    left: 218px; top: 122px;
    width: 752px; height: 430px;
    background: linear-gradient(160deg, var(--sky), var(--sky-deep));
  }
  .wordmark {
    position: absolute;
    left: 0; right: 0;
    text-align: center;
    color: var(--ink);
    font-family: var(--text-font);
    font-weight: 400;
    line-height: 1.15;
  }
  .card--front .wordmark { top: 218px; font-size: 36px; }
  .front-url {
    position: absolute;
    left: 0; right: 0; top: 380px;
    text-align: center;
    font-size: 22px;
    letter-spacing: 0.5px;
    color: var(--ink);
    white-space: nowrap;
  }

  /* Back */
  .card--back {
    left: 213px; top: 644px;
    width: 761px; height: 434px;
    display: flex;
    background: var(--ink);
  }
  .back-brand {
    position: relative;
    width: 340px; height: 100%;
    background: linear-gradient(160deg, var(--sky), var(--sky-deep));
  }
  .card--back .wordmark { top: 196px; font-size: 28px; padding: 0 16px; }
  .back-divider { width: 6px; height: 100%; background: var(--divider); }
  .back-details {
    position: relative;
    flex: 1;
    color: var(--paper-white);
    padding: 84px 0 0 26px;
  }
  .person-name { font-size: 31px; font-weight: 400; line-height: 1; white-space: nowrap; }
  .person-role { font-size: 25px; line-height: 1.1; margin-top: 4px; }
  .address { margin-top: 30px; font-size: 22px; line-height: 33px; font-style: normal; }
  .contacts { list-style: none; margin-top: 18px; font-size: 20px; }
  .contacts li { display: flex; align-items: center; height: 29px; white-space: nowrap; }
  .contacts svg { flex: none; width: 16px; height: 16px; margin-right: 8px; fill: none; stroke: var(--sky); stroke-width: 1.6; }
  .contacts .solid { fill: var(--sky); stroke: none; }
</style>
</head>
<body>
<main class="canvas">

  <section class="card card--front" aria-label="Card front">
    <p class="wordmark">Granite, Zinc &amp; Clay<br>Roofing</p>
    <p class="front-url">www.granitezincandclayroofing.example</p>
  </section>

  <section class="card card--back" aria-label="Card back">
    <div class="back-brand">
      <p class="wordmark">Granite, Zinc &amp; Clay<br>Roofing</p>
    </div>
    <div class="back-divider"></div>
    <div class="back-details">
      <h1 class="person-name">Laszlo (Les) Varga</h1>
      <p class="person-role">Owner</p>
      <address class="address">
        2871 Millbrook Rd.<br>
        Millbrook, OH 44000
      </address>
      <ul class="contacts">
        <li>
          <svg viewBox="0 0 16 16" aria-hidden="true"><path class="solid" d="M3 1.5l3 .5 1 3.5-2 1.3a9 9 0 0 0 4.2 4.2l1.3-2 3.5 1 .5 3-2 1.5C7 14 2 9 1.5 3.5z"/></svg>
          (440)555-0137
        </li>
        <li>
          <svg viewBox="0 0 16 16" aria-hidden="true"><circle cx="8" cy="8" r="6.5"/><ellipse cx="8" cy="8" rx="3" ry="6.5"/><path d="M1.5 8h13M2.5 4.8h11M2.5 11.2h11"/></svg>
          www.granitezincandclayroofing.example
        </li>
        <li>
          <svg viewBox="0 0 16 16" aria-hidden="true"><rect class="solid" x="1" y="3.5" width="14" height="9"/><path d="M1 3.5l7 5 7-5" stroke="#0c0c0c"/></svg>
          gzcroofingllc@example.com
        </li>
      </ul>
    </div>
  </section>

</main>
</body>
</html>
```